Advertising company unique advertising platform

we need a logo design for a new company based in Australia Melbourne. We develop innovated advertising platform where consumer can use this platform to get regular discount, as business owner they can use this platform for free advertisement. Payment for this advertisement platform only payable every two weeks, when I generate revenue for their business

Industry/Entity Type

Advertising

Contact Information for Business Card

Dale Morrow | Co-Founder |Managing Director
Suite 318 274 Bramwell Lane Melbourne Vic 3000

ABN 62 914 305 718
Tel: +61 0491 258 307 | Email: dale.morrow@plovintarex.com

Font styles to use
Decorative
Script

Requirements
Must have
• Try few different design and some round corner business card
Should not have
• One round corner business card...try 4 different colour background not only black, make sure two side is designed. Be creative so imagine you are giving this to a client make sure has wow factor, if you can also try one design with engrave like all the logo, words look 3d feel
• The word Advertising Platform use attached file font

```html
<!DOCTYPE html>
<html lang="en">
<head>
<meta charset="utf-8">
<title>Trivela Exchange – Business Card</title>
<link rel="stylesheet" href="https://fonts.googleapis.com/css2?family=Open+Sans:wght@400;600;700&family=Audiowide&display=swap">
<style>
  :root {
    --stage: #0a0a0a;
    --card-dark: #2c2c2b;
    --card-dark-deep: #242423;
    --band-blue: #1f5a93;
    --blue-light: #2c629a;
    --blue-deep: #17507f;
    --orange: #f7931e;
    --ink-light: #e6e6e6;
    --emboss-dark: #333331;
    --emboss-blue: #1e4e86;
  }
  * { box-sizing: border-box; margin: 0; padding: 0; }
  html, body { width: 1200px; height: 1000px; overflow: hidden; background: var(--stage); }
  .stage {
    position: relative; width: 1200px; height: 1000px;
    display: flex; align-items: center; justify-content: center; gap: 40px;
  }
  .card {
    position: relative; width: 500px; height: 286px;
    border-radius: 22px; overflow: hidden;
    box-shadow: 0 10px 30px rgba(0,0,0,.6);
  }

  /* Front: contact side */
  .card--front {
    background: linear-gradient(var(--band-blue) 0 14px, var(--card-dark) 14px calc(100% - 14px), var(--band-blue) calc(100% - 14px));
  }
  .card--front .brand {
    position: absolute; left: 30px; top: 34px;
    display: flex; align-items: center; gap: 8px;
  }
  .brand__dot { width: 22px; height: 22px; border-radius: 50%; background: var(--orange); }
  .brand__name {
    font-family: "Open Sans", sans-serif; font-weight: 700; font-size: 17px;
    color: var(--orange); letter-spacing: .3px;
  }
  .holder { position: absolute; left: 30px; top: 80px; font-family: "Open Sans", sans-serif; }
  .holder__name { color: var(--orange); font-weight: 700; font-size: 16px; }
  .holder__role { color: var(--ink-light); font-size: 11.5px; margin-top: 2px; }
  .contacts { position: absolute; left: 30px; top: 132px; list-style: none; font-family: "Open Sans", sans-serif; color: var(--ink-light); font-size: 11.5px; line-height: 17px; }
  .contacts li { display: flex; align-items: flex-start; gap: 7px; }
  .contacts svg { width: 10px; height: 10px; margin-top: 4px; flex: none; fill: var(--orange); }
  .contacts .indent { padding-left: 17px; }
  .social {
    position: absolute; right: 26px; bottom: 30px;
    display: flex; align-items: center; gap: 6px;
    font-family: "Open Sans", sans-serif; font-size: 11.5px; color: var(--ink-light);
  }
  .social__dot { width: 12px; height: 12px; border-radius: 50%; background: var(--orange); }
  .emboss-mark {
    position: absolute; right: 40px; top: 70px; text-align: right;
    font-family: "Open Sans", sans-serif; font-weight: 700; font-size: 34px; line-height: 38px;
    color: var(--emboss-dark); text-shadow: 1px 1px 0 var(--card-dark-deep), -1px -1px 0 #3a3a38;
  }

  /* Back: brand side */
  .card--back { background: linear-gradient(135deg, var(--blue-light), var(--blue-deep)); }
  .card--back .brand { position: absolute; left: 36px; top: 100px; display: flex; align-items: center; gap: 10px; }
  .card--back .brand__dot { width: 40px; height: 40px; }
  .card--back .brand__name { font-size: 26px; }
  .tagline {
    position: absolute; left: 36px; top: 166px;
    font-family: "Audiowide", sans-serif; font-size: 14px; color: var(--orange); letter-spacing: 1.5px; text-transform: uppercase;
  }
  .website {
    position: absolute; right: 28px; bottom: 30px;
    font-family: "Audiowide", sans-serif; font-size: 15px; color: var(--orange); letter-spacing: 1.5px;
  }
  .card--back .emboss-mark {
    right: 34px; top: 60px; font-size: 30px; line-height: 34px;
    color: var(--emboss-blue); text-shadow: 1px 1px 0 #174574, -1px -1px 0 #2a5f96;
  }
</style>
</head>
<body>
<main class="stage">
  <section class="card card--front" aria-label="Business card front">
    <div class="brand"><span class="brand__dot"></span><span class="brand__name">Trivela Exchange</span></div>
    <div class="emboss-mark" aria-hidden="true">Trivela<br>Exchange</div>
    <div class="holder">
      <p class="holder__name">Dale Morrow</p>
      <p class="holder__role">Co-Founder | Managing Director</p>
    </div>
    <ul class="contacts">
      <li><svg viewBox="0 0 10 10"><path d="M2 0l2 2-1 1.5c.8 1.6 1.9 2.7 3.5 3.5L8 6l2 2-1.5 2C4 10 0 6 0 1.5z"/></svg>+61 0491 258 307</li>
      <li><svg viewBox="0 0 10 10"><path d="M0 2h10v6H0zM0 2l5 3.5L10 2" /></svg>dale.morrow@plovintarex.com</li>
      <li><svg viewBox="0 0 10 10"><path d="M5 0a3.5 3.5 0 0 1 3.5 3.5C8.5 6 5 10 5 10S1.5 6 1.5 3.5A3.5 3.5 0 0 1 5 0zm0 2a1.5 1.5 0 1 0 0 3 1.5 1.5 0 0 0 0-3z"/></svg>Suite 318 274 Bramwell Lane</li>
      <li class="indent">Melbourne Vic 3000</li>
    </ul>
    <div class="social"><span class="social__dot"></span>PlovintarexShoppingStyle</div>
  </section>

  <section class="card card--back" aria-label="Business card back">
    <div class="emboss-mark" aria-hidden="true">Trivela<br>Exchange</div>
    <div class="brand"><span class="brand__dot"></span><span class="brand__name">Trivela Exchange</span></div>
    <p class="tagline">Advertising Platform</p>
    <p class="website">www.plovintarex.com</p>
  </section>
</main>
</body>
</html>
```